Business Card Design

I run an executive search and head hunting company.
My areas of business is within financial services and I cover, primarily sales and trading.

I am looking for a double sided, black business card and would like to keep the design fairly simple. Name to front and details on the reverse.

I would require a logo - some logo ideas.

*****Just some idea I am playing with - a white out halo over the "i" in Holloway.
A quill or feather somewhere within the layout. Above the Holloway Pierce & Tandy ? beneath it ? etc......

I have attached something I quite like but the whole creativity and layout is down to you. I am thinking to have the "&" in between Holloway Pierce & Tandy, maybe white out perhaps and may have it spot gloss uv'd when it comes to print.

I am pretty open minded though !

Target Market(s)

financial services - brokers and investment banking

Industry/Entity Type

Financial

Contact Information for Business Card

Holloway Pierce & Tandy
No 9 The Cloisters
52 Wexcombe Lane
Brentwood
Essex
CM17 8RT

Telephone - + 44 (0)1277 639 805
Mobile -+ 44 (0) 7623 970 315
email - oliver@hollowaypiercetandy.co.uk
web - www.hollowaypiercetandy.co.uk

Oliver Tandy
Managing Director

Colors

Designer to choose colors to be used in the design.

Requirements
Should not have
• Finance - brokers investment banking.

```html
<!DOCTYPE html>
<html lang="en">
<head>
<meta charset="utf-8">
<title>Holloway Pierce &amp; Tandy – Business Card</title>
<link rel="stylesheet" href="https://fonts.googleapis.com/css2?family=Source+Sans+3:wght@400;600;700&display=swap">
<style>
  :root {
    --backdrop: #3a3431;
    --card: #111111;
    --card-edge: #1c1c1c;
    --gloss: #4a4a4a;
    --ink-white: #f2f2f2;
    --ink-light: #c9c9c9;
    --ink-muted: #9a9a9a;
  }
  * { margin: 0; padding: 0; box-sizing: border-box; }
  html, body {
    width: 1200px; height: 716px; overflow: hidden;
    background: var(--backdrop);
    font-family: "Source Sans 3", sans-serif;
  }
  .stage {
    position: relative; width: 1200px; height: 716px;
    display: flex; align-items: center; justify-content: center; gap: 60px;
  }
  .card {
    position: relative; width: 500px; height: 286px;
    background: var(--card);
    border: 1px solid var(--card-edge);
    box-shadow: 0 10px 30px rgba(0,0,0,.45);
  }
  /* Front */
  .front-name {
    position: absolute; left: 44px; top: 62px;
    font-weight: 700; font-size: 50px; line-height: 1.02;
    color: var(--gloss); letter-spacing: -0.5px;
  }
  .front-url {
    position: absolute; left: 46px; top: 196px;
    font-size: 19px; letter-spacing: 3.2px; color: var(--ink-light);
  }
  /* Back */
  .back-logo {
    position: absolute; left: 30px; top: 26px;
    font-weight: 700; font-size: 22px; color: var(--gloss);
  }
  .person { position: absolute; left: 30px; top: 88px; }
  .person-name { font-weight: 700; font-size: 22px; color: var(--ink-white); line-height: 1; }
  .person-title { font-size: 10px; color: var(--ink-muted); margin-top: 3px; }
  .address {
    position: absolute; left: 30px; top: 150px;
    font-size: 10.5px; line-height: 1.45; color: var(--ink-muted);
  }
  .contacts {
    position: absolute; right: 22px; bottom: 22px;
    list-style: none; text-align: right;
    font-size: 11.5px; line-height: 1; color: var(--ink-light);
  }
  .contacts li {
    display: flex; justify-content: flex-end; align-items: center;
    gap: 8px; height: 19px;
  }
  .contacts svg { width: 11px; height: 11px; fill: none; stroke: var(--ink-white); stroke-width: 1.4; }
</style>
</head>
<body>
<main class="stage">
  <section class="card card-front" aria-label="Card front">
    <h1 class="front-name">Holloway Pierce<br>&amp; Tandy</h1>
    <p class="front-url">www.hollowaypiercetandy.co.uk</p>
  </section>

  <section class="card card-back" aria-label="Card back">
    <p class="back-logo">Holloway Pierce &amp; Tandy</p>
    <div class="person">
      <p class="person-name">Oliver Tandy</p>
      <p class="person-title">Managing Director</p>
    </div>
    <p class="address">No 9 The Cloisters 52 Wexcombe Lane<br>Brentwood Essex CM17 8RT</p>
    <ul class="contacts">
      <li>+ 44 (0)1277 639 805
        <svg viewBox="0 0 12 12"><path d="M2 1.5l2 .2 1 2.3-1.2 1a6 6 0 0 0 3.2 3.2l1-1.2 2.3 1 .2 2C7 11 1 5 2 1.5z" fill="var(--ink-white)" stroke="none"/></svg></li>
      <li>+ 44 (0) 7623 970 315
        <svg viewBox="0 0 12 12"><rect x="3.5" y="1" width="5" height="10" rx="1"/></svg></li>
      <li>oliver@hollowaypiercetandy.co.uk
        <svg viewBox="0 0 12 12"><rect x="1" y="2.5" width="10" height="7"/><path d="M1 2.5l5 4 5-4"/></svg></li>
      <li>www.hollowaypiercetandy.co.uk
        <svg viewBox="0 0 12 12"><circle cx="6" cy="6" r="5"/><ellipse cx="6" cy="6" rx="2.2" ry="5"/><path d="M1 6h10"/></svg></li>
    </ul>
  </section>
</main>
</body>
</html>
```